Business card design needed

We need a new business card design to re launch my carpentry business. Could include double sided card with list of services provided.
Kitchens, bathrooms, decks, pergolas, window replacements, timber floor installation, owner builder assistance and general carpentry.
Would like an eye catching card that becons to be read in bright colors that has a logo that could be also used on clothing vehicle sinage etc
Preferably in blues and reds we live near beach so maybe some type of Beecher feel
Target Market(s)
The target market of my business would be mainly individuals requiring professional carpentry services not just a handy man. The renovation market plays a big part of my business
Industry/Entity Type
Carpentry
Contact Information for Business Card
Carpenter & joiner
Rob Pelham
Tarnhaven
gilda_robbo@tarnmail.com
0439862150
Look and feel
Each slider illustrates characteristics of the customer's brand and the style your logo design should communicate.

```html
<!DOCTYPE html>
<html lang="en">
<head>
<meta charset="utf-8">
<title>Rob Pelham Carpentry – Business Card</title>
<link rel="stylesheet" href="https://fonts.googleapis.com/css2?family=Mulish:wght@700;800&family=Questrial&family=Arimo&display=swap">
<style>
  :root {
    --page-bg: #ffffff;
    --label-ink: #333333;
    --card-red-light: #ab2326;
    --card-red-mid: #8e1b1d;
    --card-red-dark: #661214;
    --card-ink: #ffffff;
    --ink-shadow: rgba(40, 0, 0, 0.75);
  }
  html, body {
    margin: 0;
    padding: 0;
    width: 1194px;
    height: 1200px;
    overflow: hidden;
    background: var(--page-bg);
  }
  .sheet {
    position: relative;
    width: 1194px;
    height: 1200px;
  }
  .side-label {
    position: absolute;
    left: 0;
    font-family: "Arimo", Arial, sans-serif;
    font-size: 24px;
    color: var(--label-ink);
    text-decoration: underline;
    text-underline-offset: 3px;
    text-decoration-thickness: 1px;
    letter-spacing: 0.2px;
  }
  .side-label--front { top: 521px; left: 0; }
  .side-label--back { top: 630px; left: 9px; }

  .card {
    position: absolute;
    left: 155px;
    width: 1039px;
    color: var(--card-ink);
    text-align: center;
    overflow: hidden;
  }
  .card--front { top: 0; height: 593px; }
  .card--back { top: 606px; height: 594px; }

  .card__wood {
    position: absolute;
    inset: 0;
    background:
      radial-gradient(ellipse 60% 75% at 50% 45%, var(--card-red-light) 0%, var(--card-red-mid) 60%, var(--card-red-dark) 100%);
  }
  .card__content {
    position: absolute;
    inset: 0;
  }
  .card__title {
    position: absolute;
    top: 213px;
    left: 0;
    right: 0;
    margin: 0;
    font-family: "Mulish", "Century Gothic", sans-serif;
    font-weight: 800;
    font-size: 34px;
    letter-spacing: 2px;
    white-space: nowrap;
    text-shadow: 2px 2px 3px var(--ink-shadow);
  }
  .card__contact {
    position: absolute;
    top: 466px;
    left: 0;
    right: 0;
    font-family: "Questrial", "Century Gothic", sans-serif;
    line-height: 39px;
    text-shadow: 1px 1px 2px var(--ink-shadow);
  }
  .card__contact span { display: block; white-space: nowrap; }
  .card__email { font-size: 33px; letter-spacing: 2.7px; }
  .card__phone { font-size: 31px; letter-spacing: 1.3px; }

  .services {
    position: absolute;
    top: 146px;
    left: 0;
    right: 0;
    margin: 0;
    padding: 0;
    list-style: none;
    font-family: "Mulish", "Century Gothic", sans-serif;
    font-weight: 800;
    font-size: 31px;
    line-height: 39.6px;
    letter-spacing: 1px;
    text-shadow: 2px 2px 3px var(--ink-shadow);
  }
</style>
</head>
<body>
<div class="sheet">
  <div class="side-label side-label--front">FRONT SIDE</div>
  <div class="side-label side-label--back">BACK SIDE</div>

  <section class="card card--front">
    <div class="card__wood" role="img" aria-label="Red stained timber plank texture"></div>
    <div class="card__content">
      <h1 class="card__title">Carpenter &amp; joiner Rob Pelham Tarnhaven</h1>
      <div class="card__contact">
        <span class="card__email">gilda_robbo@tarnmail.com</span>
        <span class="card__phone">0439862150</span>
      </div>
    </div>
  </section>

  <section class="card card--back">
    <div class="card__wood" role="img" aria-label="Red stained timber plank texture"></div>
    <div class="card__content">
      <ul class="services">
        <li>Kitchens</li>
        <li>Bathrooms</li>
        <li>Decks</li>
        <li>Pergolas</li>
        <li>Window replacements</li>
        <li>Timber floor installation</li>
        <li>Owner builder assistance</li>
        <li>General carpentry</li>
      </ul>
    </div>
  </section>
</div>
</body>
</html>
```